Creation of a Nutrition Consulting Flyer. For more information please see attached word document.

Industry/Entity Type

Health Service

Requirements
Must have
• Contend please see word document
The 3 fold flyer must meet the requirements of the DL formats, which is 210mm x 99 mm or for non 3 fold flyers DIN A 5 which is 210 mm x 148 mm (folded or non folded).
Nice to have
• our current idea is a 3 fold flyer but i am more than happy to receive other formats that better present the contend provided.

```html
<!DOCTYPE html>
<html lang="en">
<head>
<meta charset="utf-8">
<title>Nutrition Coaching – DL Trifold Flyer</title>
<link rel="stylesheet" href="https://fonts.googleapis.com/css2?family=Archivo+Black&family=Poppins:ital,wght@0,300;0,400;0,500;0,600;0,700;1,400&family=Amatic+SC:wght@700&display=swap">
<style>
  :root {
    --sheet-top: #f4f4f4;
    --sheet-bottom: #d9dadb;
    --ink: #111111;
    --blue: #566e98;
    --green: #78c46a;
    --white: #ffffff;
    --card: rgba(255,255,255,0.82);
    --fold: #8a8a8a;
    --motto-green: #7ab66b;
    --motto-ink: #2b2b2b;
  }
  * { box-sizing: border-box; margin: 0; padding: 0; }
  html, body { width: 789px; height: 1200px; overflow: hidden; }
  body {
    position: relative;
    background: linear-gradient(180deg, var(--sheet-top), var(--sheet-bottom));
    font-family: "Poppins", sans-serif;
    color: var(--ink);
  }
  .side-label {
    position: absolute;
    font-family: "Archivo Black", sans-serif;
    font-size: 42px;
    line-height: 1;
    letter-spacing: 0.5px;
  }
  .label-inside { left: 96px; top: 47px; }
  .label-back { left: 320px; top: 596px; }
  .label-front { left: 530px; top: 596px; }
  .label-outside { left: 298px; top: 1113px; }
  .outside-rule {
    position: absolute; top: 1133px; height: 1.5px; background: var(--ink);
  }
  .fold-line {
    position: absolute; top: 0; height: 1200px; width: 0;
    border-left: 1px dashed var(--fold);
    z-index: 5;
  }

  .spread {
    position: absolute; left: 88px; width: 614px;
    box-shadow: 0 14px 14px -10px rgba(0,0,0,0.35);
  }
  .spread-inside { top: 106px; height: 432px; overflow: hidden; }
  .inside-photo {
    position: absolute; inset: 0;
    background:
      radial-gradient(ellipse 42% 60% at 72% 58%, #e03a2b 0%, #d23526 55%, rgba(210,53,38,0) 75%),
      radial-gradient(ellipse 30% 25% at 62% 18%, #4f7a3a 0%, rgba(79,122,58,0) 70%),
      linear-gradient(90deg, #efe4d8 0%, #eadccd 45%, #e8d4c2 100%);
  }
  .quote {
    position: absolute; left: 38px; top: 140px;
    font-size: 37px; line-height: 37px; font-weight: 300; letter-spacing: -0.5px;
  }
  .quote-mark {
    font-family: "Archivo Black", sans-serif; font-size: 56px; line-height: 1;
    display: block; height: 44px; margin-bottom: 14px;
  }
  .quote strong { font-weight: 700; }

  .step {
    position: absolute; left: 354px; width: 240px;
    display: flex;
  }
  .step-no {
    width: 56px; background: var(--white);
    font-weight: 600; font-size: 39px; line-height: 1;
    display: flex; align-items: center; justify-content: center;
  }
  .step-text {
    flex: 1; background: var(--card);
    padding: 6px 14px 4px 16px;
    font-size: 5.8px; line-height: 8.6px; font-style: italic;
  }
  .step-1 { top: 154px; height: 55px; }
  .step-1 .step-text { overflow: hidden; }
  .step-2 { top: 218px; height: 46px; }
  .step-3 { top: 275px; height: 117px; }

  .spread-outside { top: 653px; height: 435px; display: flex; }
  .panel { position: relative; height: 100%; }
  .panel-about { width: 205px; background: var(--blue); color: var(--white); text-align: center; }
  .portrait {
    position: absolute; left: 41px; top: 71px; width: 122px; height: 122px;
    border-radius: 50%; border: 3px solid var(--white);
    background: radial-gradient(circle at 50% 45%, #c9b9a8, #8c8f86 60%, #3f6b35);
  }
  .about-name { position: absolute; top: 216px; width: 100%; font-size: 14px; font-weight: 600; }
  .about-copy {
    position: absolute; left: 18px; right: 18px; font-size: 8.4px; line-height: 10.5px; font-style: italic;
  }
  .about-copy-1 { top: 240px; }
  .about-copy-2 { top: 293px; }

  .panel-services { width: 204px; background: var(--green); color: var(--white); padding-left: 27px; }
  .services-title {
    position: absolute; left: 27px; top: 674px; top: 22px;
    font-size: 42px; font-weight: 700; line-height: 38px; letter-spacing: -0.3px;
  }
  .services-list {
    position: absolute; left: 27px; top: 191px; width: 170px;
    list-style: none; font-size: 7.6px; line-height: 11.8px;
  }
  .services-list li { padding-left: 8px; position: relative; }
  .services-list li::before { content: "•"; position: absolute; left: 0; }
  .services-list li.two-line { line-height: 8px; padding-top: 2px; padding-bottom: 2px; }
  .services-info { position: absolute; left: 27px; top: 292px; width: 150px; font-size: 7.6px; line-height: 9.6px; }
  .tag {
    position: absolute; left: 28px; background: var(--white); color: var(--green);
    font-weight: 500; white-space: nowrap;
  }
  .tag-web { top: 328px; width: 145px; height: 16px; font-size: 11.5px; line-height: 16px; padding-left: 5px; }
  .services-name { position: absolute; left: 27px; top: 351px; font-size: 17px; font-weight: 600; }
  .services-contact { position: absolute; left: 27px; top: 375px; font-size: 7.4px; line-height: 11.5px; }
  .tag-hours {
    top: 403px; width: 146px; height: 21px; background: transparent;
    border: 1.5px solid var(--white); color: var(--white);
    font-size: 12px; line-height: 18px; text-align: center;
  }

  .panel-cover { width: 205px; overflow: hidden; }
  .cover-photo {
    position: absolute; inset: 0;
    background:
      radial-gradient(ellipse 45% 22% at 50% 78%, #f4f2ee 0%, rgba(244,242,238,0) 80%),
      radial-gradient(ellipse 70% 40% at 40% 55%, #d99a3f 0%, #b58f5a 50%, rgba(181,143,90,0) 80%),
      linear-gradient(180deg, #dcd9d2 0%, #c9b48f 45%, #a9b9bd 100%);
  }
  .cover-arc { position: absolute; left: 0; top: 0; }
  .motto {
    position: absolute; right: 25px; top: 28px; text-align: right;
    font-family: "Amatic SC", cursive; font-size: 22px; line-height: 27px; color: var(--motto-ink);
  }
  .motto .accent { color: var(--motto-green); }
  .cover-caption {
    position: absolute; left: 15px; top: 408px; width: 176px; height: 17px;
    background: var(--white); font-size: 10px; font-weight: 500; line-height: 17px; text-align: center;
  }
</style>
</head>
<body>
  <div class="fold-line" style="left:291px"></div>
  <div class="fold-line" style="left:496px"></div>

  <h2 class="side-label label-inside">INSIDE</h2>

  <section class="spread spread-inside">
    <div class="inside-photo" role="img" aria-label="Close-up photo of a red strawberry with green leaves on a cream background"></div>
    <p class="quote">
      <span class="quote-mark">“</span>
      My aim is,<br><strong>to perfectly</strong><br>support you<br><strong>to achieve</strong><br>your aims.
    </p>
    <div class="step step-1">
      <div class="step-no">1</div>
      <p class="step-text">I offer personal as well as online coaching. We could meet at your place, in a café, at my place or online via multiple channels. As your personal coach I will be available to answer your questions or solve your questions in a responsible and</p>
    </div>
    <div class="step step-2">
      <div class="step-no">2</div>
      <p class="step-text">One of the most effective ways you can take to improve your health is to increase your energy level and to prevent chronical diseases, is to alter to a healthy and nutrition diet.</p>
    </div>
    <div class="step step-3">
      <div class="step-no">3</div>
      <p class="step-text">Whenever there is a desire to change the current condition, coaching can support you on boost this desire for a change to the better. Using suitable questions and tools, we will define your aims and define measures to achieve your goals. You will understand, on what can be changed in your nutrition in order to make the change sustainable. My holistic nutrition coaching is fully tailored to your needs and circumstances. You are the one determining on what shall be done and in which speed. And with my consultation, I am positive that you will master your challenge.</p>
    </div>
  </section>

  <h2 class="side-label label-back">BACK</h2>
  <h2 class="side-label label-front">FRONT</h2>

  <section class="spread spread-outside">
    <div class="panel panel-about">
      <div class="portrait" role="img" aria-label="Round portrait photo of the nutrition coach holding fresh herbs"></div>
      <h3 class="about-name">Dr. Lena Berger,</h3>
      <p class="about-copy about-copy-1">Diplom-Ökotrophologin<br>Starting at my childhood, nutrition started to play a major role in my life.</p>
      <p class="about-copy about-copy-2">I was fascinated, on how much potential our daily life food has on our health. This knowledge I have gained during my career is what I would like to pass on to as many people as possible to profit from the enormous profits of a healthy diet.</p>
    </div>

    <div class="panel panel-services">
      <h3 class="services-title">I<br>advise<br>you<br>on</h3>
      <ul class="services-list">
        <li>Questions about a healthy diet</li>
        <li>Your aim to lose weight</li>
        <li>Nutrition during pregnancy</li>
        <li>Nutrition during nursing</li>
        <li class="two-line">Preparation of beneficial dishes for the whole family</li>
        <li>Intestinal health</li>
      </ul>
      <p class="services-info">Information on my coaching offers, the process as well as pricing can be found on my homepage:</p>
      <span class="tag tag-web">www.gutessen.blog</span>
      <p class="services-name">Dr. Lena Berger</p>
      <p class="services-contact">kontakt@gutessen.blog<br>06201 5550142</p>
      <span class="tag tag-hours">(Mo-Fr 9.00-12.00 Uhr)</span>
    </div>

    <div class="panel panel-cover">
      <div class="cover-photo" role="img" aria-label="Photo of the coach holding a bowl of strawberries in front of a colourful bowl of roasted vegetables and grains"></div>
      <svg class="cover-arc" width="205" height="170" viewBox="0 0 205 170" aria-hidden="true">
        <path d="M32 0 H205 V158 C150 160 80 140 50 95 C30 65 28 30 32 0 Z" fill="#f7f8f9"/>
      </svg>
      <p class="motto">Increase in<br><span class="accent">quality of live based</span><br>on nutrition<br><span class="accent">is my motto.</span></p>
      <p class="cover-caption">Wellbeing – life quality – health</p>
    </div>
  </section>

  <div class="outside-rule" style="left:88px;width:194px"></div>
  <h2 class="side-label label-outside">OUTSIDE</h2>
  <div class="outside-rule" style="left:508px;width:194px"></div>
</body>
</html>
```